Business Card Design Project

Looking for a simple and stylish business card. We are an Advertising Company. The card Must feature the company logo (attached) and also this info.
p: 0481629054
e: sales@rv-promo.com.au
w: www.rv-promo.com.au
We Advertise mainly using TV screens featured in restaurants and cafe. See website for more about the business.
Not really looking for a plain background, but at the same time do not want to much happening in the Background. I am not really to fussy though with the design or the colour scheme, and I am leaving the creativity part up to you creative designers.

```html
<!DOCTYPE html>
<html lang="en">
<head>
<meta charset="utf-8">
<title>RV Promo – Business Card</title>
<link rel="stylesheet" href="https://fonts.googleapis.com/css2?family=Hind:wght@300;400;500;600&display=swap">
<style>
  :root {
    --stage-bg: #ece8e2;
    --brand-blue: #164d97;
    --brand-pink: #e31c5d;
    --band-white: #f4f6f4;
    --card-cream: #fcf8f3;
    --text-light: #ffffff;
  }
  * { margin: 0; padding: 0; box-sizing: border-box; }
  html, body {
    width: 1200px;
    height: 900px;
    overflow: hidden;
    background: var(--stage-bg);
    font-family: "Hind", Arial, sans-serif;
  }
  .business-card {
    position: absolute;
    left: 432px;
    top: 156px;
    width: 336px;
    height: 587px;
    overflow: hidden;
    background: var(--card-cream);
  }
  .card-bands {
    position: absolute;
    inset: 0;
    width: 336px;
    height: 587px;
  }
  .band-blue { fill: var(--brand-blue); }
  .band-white { fill: var(--band-white); }
  .band-pink { fill: var(--brand-pink); }
  .band-cream { fill: var(--card-cream); }
  .holder {
    position: absolute;
    left: 26px;
    top: 24px;
    color: var(--text-light);
    font-weight: 600;
    font-size: 25px;
    line-height: 33px;
  }
  .holder-role,
  .holder-name { display: block; }
  .contact-list {
    position: absolute;
    right: 19px;
    top: 200px;
    list-style: none;
    text-align: right;
    color: var(--text-light);
    font-weight: 400;
    font-size: 21px;
    letter-spacing: 0.3px;
    line-height: 28.5px;
  }
  .company-name {
    position: absolute;
    left: 0;
    right: 0;
    top: 478px;
    text-align: center;
    color: var(--brand-blue);
    font-weight: 300;
    font-size: 56px;
    letter-spacing: 2px;
    line-height: 80px;
  }
</style>
</head>
<body>
  <article class="business-card">
    <svg class="card-bands" viewBox="0 0 336 587" aria-hidden="true">
      <rect class="band-blue" x="0" y="0" width="336" height="587"/>
      <polygon class="band-white" points="0,262 336,96 336,587 0,587"/>
      <polygon class="band-pink" points="0,282 336,118 336,587 0,587"/>
      <polygon class="band-blue" points="0,478 336,300 336,587 0,587"/>
      <polygon class="band-cream" points="0,498 336,322 336,587 0,587"/>
    </svg>

    <h1 class="holder">
      <span class="holder-role">Managing Director</span>
      <span class="holder-name">Daniel Mercer</span>
    </h1>

    <ul class="contact-list">
      <li class="contact-phone">0481629054</li>
      <li class="contact-email">sales@rv-promo.com.au</li>
      <li class="contact-web">www.rv-promo.com.au</li>
    </ul>

    <p class="company-name">RVPROMO</p>
  </article>
</body>
</html>
```